Re-Design an adult education portal

I need support to re-design an adult education portal. Currently the customer has an incomplete website which should be prepared in a new format.
I have the idea how to realize, but I have no clue how to design it. The hard thing is to have a "beautiful" website with available logo and main color. I hope you can support me.

Name of Website: tovelu (tovelu.example)
Content: adult eduction for adult in safety at work, mountain climbing, dog school. various courses in different areas. But on old webpage is hard to find the different possibilities.
main color: Ral 6011 (green) -> #6C7C59
logo: you see on top of website the logo (2 dogs and a mountain with a colour gradient).

new website: for new webpage I decided to have a navigation for each section of education. In the main area I would like to have some pictures to give an idea what content is behind. At the moment it looks terrible, so I decided to use you as support for me to make the webpage prettier :). And maybe you have an better idea how to make it great. -> current state of new web page: https://tovelu.brisk-host.example/

Target Market(s)

adult eduction for adult in safety at work, mountain climbing, dog school

Number of Pages Required

1 page

Font styles to use
Serif
Sans Serif

Requirements
Must have
• As main color is set "Ral 6011" (green) -> #6C7C59

```html
<!DOCTYPE html>
<html lang="en">
<head>
<meta charset="utf-8">
<title>tovelu – Training and Course Partner</title>
<link rel="stylesheet" href="https://fonts.googleapis.com/css2?family=Outfit:wght@300;400;500;700;800&family=Arimo:wght@400;700&display=swap">
<style>
:root{
  --green:#6c7c59;
  --green-dark:#65744f;
  --ink:#2e2e2e;
  --muted:#555;
  --paper:#f4f4ef;
  --ring:#c9cdbd;
  --white:#fff;
}
*{box-sizing:border-box;margin:0;padding:0}
html,body{width:1200px;height:2985px;overflow:hidden}
body{position:relative;background:var(--white);font-family:"Outfit",sans-serif;color:var(--ink)}
.abs{position:absolute}
.site-header{position:absolute;left:0;top:0;width:1200px;height:93px;background:var(--white)}
.brand{position:absolute;left:87px;top:16px;width:182px;height:94px;background:#f1efe2;display:flex;align-items:center;justify-content:center;font-weight:500;font-size:20px;color:var(--green-dark);z-index:2}
.main-nav{position:absolute;top:48px;left:0;font-family:"Arimo",sans-serif;font-size:14px;color:#333}
.main-nav span{position:absolute;white-space:nowrap}
.main-nav span::after{content:"";display:inline-block;margin-left:4px;vertical-align:2px;border:4.5px solid transparent;border-top:5px solid var(--green);border-bottom:0}
.hero{position:absolute;left:0;top:93px;width:1200px;height:626px;background:linear-gradient(180deg,#748856 0%,#6f8255 60%,#6a7c52 100%);overflow:hidden}
.hero-title{position:absolute;left:107px;top:184px;color:var(--white);font-size:50px;line-height:54px;font-weight:800}
.hero-title .light{font-weight:500}
.hero-text{position:absolute;left:107px;top:312px;width:395px;color:var(--white);font-size:23px;line-height:30px;font-weight:300}
.about-photo{position:absolute;left:0;top:719px}
.about-title{position:absolute;left:665px;top:830px;font-size:37px;font-weight:800;color:var(--ink)}
.rule{position:absolute;height:5px;border-top:1.5px solid var(--green);border-bottom:1.5px solid var(--green)}
.about-text{position:absolute;left:678px;top:910px;width:428px;font-size:16.5px;line-height:31px;font-weight:300;color:var(--muted);hyphens:auto}
.btn{position:absolute;left:680px;top:1120px;width:171px;height:43px;border:2px solid var(--green);color:var(--green);font-size:15px;font-weight:500;display:flex;align-items:center;justify-content:center;letter-spacing:.3px}
.courses{position:absolute;left:0;top:1261px;width:1200px;height:1469px;background:var(--paper)}
.courses-title{position:absolute;left:0;width:1200px;top:65px;text-align:center;font-size:35px;font-weight:800;color:var(--ink)}
.card{position:absolute;width:305px;background:var(--white);border-radius:28px 28px 8px 8px;box-shadow:0 3px 6px rgba(0,0,0,.12);text-align:center}
.card.is-active{background:var(--green);color:var(--white)}
.card svg{position:absolute;left:22px;top:22px}
.card-label{position:absolute;left:0;width:100%;font-size:21px;font-weight:700;color:#3b3b3b}
.card.is-active .card-label{color:var(--white)}
.card-sub{position:absolute;left:40px;width:225px;top:345px;font-size:12px;line-height:17px;color:var(--white)}
.contact-band{position:absolute;left:0;top:2730px;width:1200px;height:92px;background:var(--green)}
.contact{position:absolute;top:17px;display:flex;align-items:center;gap:10px;color:var(--white)}
.contact .dot{width:58px;height:58px;border-radius:50%;background:var(--white);display:flex;align-items:center;justify-content:center}
.contact b{display:block;font-size:13.5px;font-weight:700}
.contact small{font-size:13.5px;font-weight:300}
.site-footer{position:absolute;left:0;top:2822px;width:1200px;height:163px;background:var(--green-dark);color:var(--white);text-align:center}
.foot-nav{position:absolute;top:32px;left:0;width:1200px;display:flex;justify-content:center;gap:35px;font-size:13px;font-weight:700;letter-spacing:.3px}
.copyright{position:absolute;top:70px;width:1200px;font-size:13.5px;font-weight:300}
.social{position:absolute;top:110px;left:536px;display:flex;gap:20px}
.social span{width:18px;height:18px;border-radius:3px;background:var(--white)}
</style>
</head>
<body>

<header class="site-header">
  <div class="brand">tovelu.example</div>
  <nav class="main-nav">
    <span style="left:314px">OCCUPATIONAL SAFETY</span>
    <span style="left:527px">FIRST AID</span>
    <span style="left:643px">CZV</span>
    <span style="left:721px">DOG SCHOOL</span>
    <span style="left:862px">MOUNTAIN TRAINING</span>
    <span style="left:1057px">TOVELU</span>
  </nav>
</header>

<section class="hero">
  <svg class="abs" style="left:0;top:0" width="1200" height="626" aria-hidden="true">
    <defs>
      <linearGradient id="sky" x1="0" y1="0" x2="0" y2="1"><stop offset="0" stop-color="#8fb3cf"/><stop offset="1" stop-color="#dfe9ee"/></linearGradient>
      <linearGradient id="meadow" x1="0" y1="0" x2="0" y2="1"><stop offset="0" stop-color="#8a9a70"/><stop offset=".5" stop-color="#9b7a6a"/><stop offset="1" stop-color="#6f9a3c"/></linearGradient>
    </defs>
    <path d="M0 430 Q200 360 380 420 T760 400 T1200 330 V626 H0Z" fill="#66784e" opacity=".45"/>
    <circle cx="882" cy="287" r="255" fill="none" stroke="#fff" stroke-width="6"/>
    <circle cx="882" cy="287" r="232" fill="url(#meadow)" role="img" aria-label="Photo of the two course leaders with their dog on a meadow"/>
    <circle cx="691" cy="431" r="162" fill="none" stroke="#a2b08a" stroke-width="4"/>
    <circle cx="691" cy="431" r="145" fill="#fff"/>
    <circle cx="691" cy="431" r="140" fill="url(#sky)" role="img" aria-label="Photo of a child climbing a ladder into the sky"/>
  </svg>
  <h1 class="hero-title">Your Training and<br><span class="light">Course Partner</span></h1>
  <p class="hero-text">We offer training tailored to your needs, target-oriented and tailored to your skills and knowledge .</p>
</section>

<section>
  <svg class="about-photo" width="640" height="542" aria-hidden="true">
    <defs><linearGradient id="tree" x1="0" y1="0" x2="1" y2="1"><stop offset="0" stop-color="#7c93b8"/><stop offset=".5" stop-color="#7b6a54"/><stop offset="1" stop-color="#55524a"/></linearGradient></defs>
    <path d="M548 0 Q708 271 505 542" fill="none" stroke="var(--green)" stroke-width="7"/>
    <path d="M0 0 H510 Q670 271 485 542 H0Z" fill="url(#tree)" role="img" aria-label="Photo of the course leaders with two dogs under an autumn tree"/>
  </svg>
  <h2 class="about-title">ABOUT TOVELU</h2>
  <div class="rule" style="left:678px;top:889px;width:91px"></div>
  <p class="about-text" lang="en">In my professional career, I have repeatedly experienced situations that gave me the idea of giving every interested person basic knowledge that allows them to react correctly and with the necessary calm in an emergency. The pooling and combining of knowledge and skills from the various specialist areas</p>
  <a class="btn">LEARN MORE</a>
</section>

<section class="courses">
  <svg width="0" height="0" style="position:absolute" aria-hidden="true">
    <defs>
      <linearGradient id="g-fork" x1="0" y1="0" x2="0" y2="1"><stop offset="0" stop-color="#d6d5cc"/><stop offset="1" stop-color="#9a978a"/></linearGradient>
      <linearGradient id="g-ppe" x1="0" y1="0" x2="0" y2="1"><stop offset="0" stop-color="#8d918a"/><stop offset="1" stop-color="#3d4a3a"/></linearGradient>
      <linearGradient id="g-aerial" x1="0" y1="0" x2="0" y2="1"><stop offset="0" stop-color="#6f9cd6"/><stop offset="1" stop-color="#7c7f78"/></linearGradient>
      <linearGradient id="g-dog" x1="0" y1="0" x2="0" y2="1"><stop offset="0" stop-color="#5b5a3a"/><stop offset="1" stop-color="#7ea63e"/></linearGradient>
      <linearGradient id="g-aid" x1="0" y1="0" x2="0" y2="1"><stop offset="0" stop-color="#d9dfe2"/><stop offset="1" stop-color="#a8b4ba"/></linearGradient>
      <linearGradient id="g-med" x1="0" y1="0" x2="0" y2="1"><stop offset="0" stop-color="#d7dde3"/><stop offset="1" stop-color="#5d8fc2"/></linearGradient>
      <linearGradient id="g-rail" x1="0" y1="0" x2="0" y2="1"><stop offset="0" stop-color="#a9c6e3"/><stop offset="1" stop-color="#8c8a80"/></linearGradient>
      <linearGradient id="g-truck" x1="0" y1="0" x2="0" y2="1"><stop offset="0" stop-color="#5e7d4a"/><stop offset="1" stop-color="#2a2c2c"/></linearGradient>
      <linearGradient id="g-mount" x1="0" y1="0" x2="0" y2="1"><stop offset="0" stop-color="#b9c4cf"/><stop offset="1" stop-color="#6d6a64"/></linearGradient>
    </defs>
  </svg>
  <h2 class="courses-title">OUR TRAINING COURSES</h2>
  <div class="rule" style="left:556px;top:116px;width:91px"></div>

  <div class="card" style="left:117px;top:163px;height:402px">
    <svg width="262" height="262"><circle cx="131" cy="131" r="130" fill="#fff" stroke="var(--ring)" stroke-width="2"/><circle cx="131" cy="131" r="116" fill="url(#g-fork)" role="img" aria-label="Photo of a forklift in a warehouse"/></svg>
    <div class="card-label" style="top:306px">Forklift Courses</div>
  </div>
  <div class="card is-active" style="left:450px;top:163px;height:402px">
    <svg width="262" height="262"><circle cx="131" cy="131" r="130" fill="none" stroke="#d6dccb" stroke-width="2"/><circle cx="131" cy="131" r="116" fill="url(#g-ppe)" role="img" aria-label="Photo of a worker wearing a fall-protection harness"/></svg>
    <div class="card-label" style="top:305px">PPE</div>
    <div class="card-sub">Personal protective equipment against falls from a height (PPE)</div>
  </div>
  <div class="card" style="left:786px;top:163px;height:402px">
    <svg width="262" height="262"><circle cx="131" cy="131" r="130" fill="#fff" stroke="var(--ring)" stroke-width="2"/><circle cx="131" cy="131" r="116" fill="url(#g-aerial)" role="img" aria-label="Photo of an aerial work platform beside a road"/></svg>
    <div class="card-label" style="top:306px">Aerial work platform</div>
  </div>

  <div class="card" style="left:117px;top:596px;height:380px">
    <svg width="262" height="262"><circle cx="131" cy="131" r="130" fill="#fff" stroke="var(--ring)" stroke-width="2"/><circle cx="131" cy="131" r="116" fill="url(#g-dog)" role="img" aria-label="Photo of two dogs lying in the grass"/></svg>
    <div class="card-label" style="top:302px">Dog school</div>
  </div>
  <div class="card" style="left:450px;top:596px;height:380px">
    <svg width="262" height="262"><circle cx="131" cy="131" r="130" fill="#fff" stroke="var(--ring)" stroke-width="2"/><circle cx="131" cy="131" r="116" fill="url(#g-aid)" role="img" aria-label="Photo of first aid training on manikins"/></svg>
    <div class="card-label" style="top:302px">First aiders</div>
  </div>
  <div class="card" style="left:786px;top:596px;height:380px">
    <svg width="262" height="262"><circle cx="131" cy="131" r="130" fill="#fff" stroke="var(--ring)" stroke-width="2"/><circle cx="131" cy="131" r="116" fill="url(#g-med)" role="img" aria-label="Photo of medical staff training at a patient bed"/></svg>
    <div class="card-label" style="top:306px">Medical training</div>
  </div>

  <div class="card" style="left:120px;top:999px;height:378px">
    <svg width="262" height="262"><circle cx="131" cy="131" r="130" fill="#fff" stroke="var(--ring)" stroke-width="2"/><circle cx="131" cy="131" r="116" fill="url(#g-rail)" role="img" aria-label="Photo of a passenger train"/></svg>
    <div class="card-label" style="top:308px">RAIL AGD</div>
  </div>
  <div class="card" style="left:453px;top:999px;height:378px">
    <svg width="262" height="262"><circle cx="131" cy="131" r="130" fill="#fff" stroke="var(--ring)" stroke-width="2"/><circle cx="131" cy="131" r="116" fill="url(#g-truck)" role="img" aria-label="Photo of a driving school truck"/></svg>
    <div class="card-label" style="top:302px">CZV</div>
  </div>
  <div class="card" style="left:789px;top:999px;height:378px">
    <svg width="262" height="262"><circle cx="131" cy="131" r="130" fill="#fff" stroke="var(--ring)" stroke-width="2"/><circle cx="131" cy="131" r="116" fill="url(#g-mount)" role="img" aria-label="Photo of a climber on a mountain ridge"/></svg>
    <div class="card-label" style="top:304px">Mountain training</div>
  </div>
</section>

<section class="contact-band">
  <div class="contact" style="left:176px">
    <div class="dot"><svg width="22" height="30" viewBox="0 0 22 30"><path d="M11 1C5 1 1 5.5 1 11c0 8 10 18 10 18s10-10 10-18C21 5.5 17 1 11 1z" fill="none" stroke="var(--green)" stroke-width="2.5"/><circle cx="11" cy="11" r="3.5" fill="var(--green)"/></svg></div>
    <div><b>Address</b><small>Lindenweg 27, CH-3900 Vellen</small></div>
  </div>
  <div class="contact" style="left:537px">
    <div class="dot"><svg width="28" height="22" viewBox="0 0 28 22"><path d="M2 8c0-5 24-5 24 0l-4 2-2-3H8L6 10z" fill="var(--green)"/><rect x="6" y="10" width="16" height="10" rx="2" fill="var(--green)"/><circle cx="14" cy="15" r="3" fill="#fff"/></svg></div>
    <div><b>Phone Number</b><small>+41 70 555 01 23</small></div>
  </div>
  <div class="contact" style="left:848px">
    <div class="dot"><svg width="26" height="18" viewBox="0 0 26 18"><rect x="1" y="1" width="24" height="16" fill="none" stroke="var(--green)" stroke-width="2"/><path d="M1 1l12 9 12-9" fill="none" stroke="var(--green)" stroke-width="2"/></svg></div>
    <div><b>Email address</b><small>info@tovelu.example</small></div>
  </div>
</section>

<footer class="site-footer">
  <nav class="foot-nav"><span>OCCUPATIONAL SAFETY</span><span>FIRST AID</span><span>CZV</span><span>DOG SCHOOL</span><span>MOUNTAIN TRAINING</span><span>TOVELU</span></nav>
  <p class="copyright">©2021 Copyright tovelu.example. All Right Reserved</p>
  <div class="social"><span aria-label="Social link"></span><span aria-label="Social link"></span><span aria-label="Social link"></span><span aria-label="Social link"></span></div>
</footer>

</body>
</html>
```